Design profile for MuroDeck Nordhaven

I had a logo competition here recently, and was left with two logos that I could not choose between. Therefore, I create this competition where I want a complete design package or a visual identity for the company. I want you to create design elements that can be used both in print and online. (letterhead, envelopes, business card, website, facebook, etc.) I have also attached a picture of the car I have ordered. I'm happy if you can show how the design can be used on that as well.
What is important is that the logos are treated individually, and that the design you create reflects or builds up under the logo. I want the design to be recognizable and to have a connection with the logo and what we do. (take fizzo lumo as an example. if you remove the name, but keep the red color and the white line, then you will recognize which brand it is about right away)
You choose whether you want to make proposals only for one logo, or or both, but it is important that they are treated individually. The best overall package determines which logo I use.
I have also added an image that you can use as an example background if you want it in a facebook banner for example.
It is important that the design looks professional and unique. A number of designs have come in, but many of the designs are very similar and general. Here is a video of the printer if you need inspiration: https://clipvault.example/v/Q8ZtrMx2LwK

Industry/Entity Type

WallPrinting

Requirements
Must have
• Unique an professional design that can be used both online and print
Nice to have
• Show how to use the design on a VX Tully. (see photos attached)
Should not have
• The design can be simple, but not too simple and general. I want it to give the company an identity

```html
<!DOCTYPE html>
<html lang="en">
<head>
<meta charset="utf-8">
<title>MuroDeck Nordhaven – Stationery</title>
<link rel="stylesheet" href="https://fonts.googleapis.com/css2?family=Barlow:wght@500;600&display=swap">
<style>
  :root{
    --sky:#6dd0f5;
    --cyan:#22c4f0;
    --azure:#2aaae2;
    --ocean:#0d72b9;
    --royal:#1a4aa0;
    --indigo:#253a80;
    --navy:#232d68;
    --ink:#0b0b0c;
    --black:#050506;
    --paper:#ffffff;
    --edge:#c9c9c9;
    --icon:#1b6fc2;
    --amber:#f7931e;
    --ember:#f07028;
    --brick:#c0302a;
    --wine:#7c1016;
    --maroon:#5a1418;
  }
  *{box-sizing:border-box;margin:0;padding:0}
  html,body{width:1200px;height:947px;overflow:hidden;background:var(--paper)}
  body{position:relative;font-family:"Barlow",sans-serif;font-weight:500;color:var(--ink)}

  .sheet{position:absolute;background:var(--paper);box-shadow:0 6px 14px rgba(0,0,0,.18)}
  .stripe{position:absolute;top:0;bottom:0;display:flex;flex-direction:column}
  .stripe span{flex:1}
  .stripe.left{left:0}
  .stripe.right{right:0}

  .wordmark{position:absolute;text-align:center;line-height:1.05;font-weight:600;letter-spacing:.5px}

  .contact-line{position:absolute;display:flex;align-items:center;gap:4px;white-space:nowrap;font-size:9px}
  .contact-line svg{width:8px;height:8px;flex:none}
  .contact-line .gap{width:4px}

  /* Letterhead */
  .letterhead{left:59px;top:38px;width:597px;height:845px;border:1px solid var(--edge)}
  .letterhead .stripe{width:20px}
  .letterhead .wordmark{left:0;right:0;top:78px;font-size:30px;color:var(--ink)}
  .letterhead .contact-line{left:84px;top:787px}

  /* Envelope */
  .envelope{left:407px;top:476px;width:650px;height:289px;border:1px solid var(--edge)}
  .envelope .stripe{width:20px}
  .envelope .wordmark{left:38px;top:32px;text-align:left;font-size:20px;color:var(--ink)}
  .envelope .contact-line{left:38px;top:247px}
  .flap{position:absolute;left:1056px;top:476px;width:78px;height:289px}

  /* Business cards */
  .card{position:absolute;width:259px;height:154px;background:var(--black);color:var(--paper)}
  .card .stripe{width:9px}
  .card-front{left:739px;top:83px}
  .card-front .wordmark{left:0;right:0;top:50px;font-size:18px;color:var(--paper)}
  .card-front .contact-line{left:0;right:0;justify-content:center;top:131px;font-size:7.5px}
  .card-back{left:832px;top:268px;width:256px;height:153px;background:#000}
  .card-back .details{position:absolute;left:0;right:0;top:40px;text-align:center;font-size:7.5px;line-height:1.3}
  .card-back .name{color:var(--amber);font-size:8.5px;font-weight:600}
  .card-back .pin{display:block;margin:6px auto 1px;width:7px;height:7px}
  .card-back .email{display:inline-flex;align-items:center;gap:3px;margin-top:3px}
  .card-back .email svg{width:7px;height:7px}
</style>
</head>
<body>

<!-- Letterhead -->
<section class="sheet letterhead" aria-label="Letterhead">
  <div class="stripe left">
    <span style="background:var(--sky)"></span><span style="background:var(--cyan)"></span><span style="background:var(--azure)"></span><span style="background:var(--ocean)"></span><span style="background:var(--royal)"></span><span style="background:var(--indigo)"></span><span style="background:var(--navy)"></span>
  </div>
  <div class="stripe right">
    <span style="background:var(--navy)"></span><span style="background:var(--indigo)"></span><span style="background:var(--royal)"></span><span style="background:var(--ocean)"></span><span style="background:var(--azure)"></span><span style="background:var(--cyan)"></span><span style="background:var(--sky)"></span>
  </div>
  <div class="wordmark">MuroDeck<br>Nordhaven</div>
  <div class="contact-line">
    <svg viewBox="0 0 10 10"><path d="M5 0.5a3.3 3.3 0 0 0-3.3 3.3C1.7 6.3 5 9.5 5 9.5s3.3-3.2 3.3-5.7A3.3 3.3 0 0 0 5 .5z" fill="var(--icon)"/><circle cx="5" cy="3.8" r="1.2" fill="#fff"/></svg>
    <span>Lorem Ipsum Dolor sit Amet, Consectetuer, Dolor sit Amet.</span><span class="gap"></span>
    <svg viewBox="0 0 10 10"><rect x=".8" y="2" width="8.4" height="6" fill="none" stroke="var(--icon)" stroke-width="1"/><path d="M.8 2.3 5 5.6l4.2-3.3" fill="none" stroke="var(--icon)" stroke-width="1"/></svg>
    <span>hello@murodeck.example</span><span class="gap"></span>
    <svg viewBox="0 0 10 10"><circle cx="5" cy="5" r="4.2" fill="none" stroke="var(--icon)" stroke-width="1"/><ellipse cx="5" cy="5" rx="1.8" ry="4.2" fill="none" stroke="var(--icon)" stroke-width=".8"/><path d="M.8 5h8.4" stroke="var(--icon)" stroke-width=".8"/></svg>
    <span>www.murodeck.example</span>
  </div>
</section>

<!-- Envelope -->
<section class="sheet envelope" aria-label="Envelope">
  <div class="stripe left">
    <span style="background:var(--navy)"></span><span style="background:var(--indigo)"></span><span style="background:var(--royal)"></span><span style="background:var(--ocean)"></span><span style="background:var(--azure)"></span><span style="background:var(--cyan)"></span><span style="background:var(--sky)"></span>
  </div>
  <div class="wordmark">MuroDeck<br>Nordhaven</div>
  <div class="contact-line">
    <svg viewBox="0 0 10 10"><path d="M5 0.5a3.3 3.3 0 0 0-3.3 3.3C1.7 6.3 5 9.5 5 9.5s3.3-3.2 3.3-5.7A3.3 3.3 0 0 0 5 .5z" fill="var(--icon)"/><circle cx="5" cy="3.8" r="1.2" fill="#fff"/></svg>
    <span>Lorem Ipsum Dolor sit Amet, Consectetuer, Dolor sit Amet.</span><span class="gap"></span>
    <svg viewBox="0 0 10 10"><rect x=".8" y="2" width="8.4" height="6" fill="none" stroke="var(--icon)" stroke-width="1"/><path d="M.8 2.3 5 5.6l4.2-3.3" fill="none" stroke="var(--icon)" stroke-width="1"/></svg>
    <span>hello@murodeck.example</span><span class="gap"></span>
    <svg viewBox="0 0 10 10"><circle cx="5" cy="5" r="4.2" fill="none" stroke="var(--icon)" stroke-width="1"/><ellipse cx="5" cy="5" rx="1.8" ry="4.2" fill="none" stroke="var(--icon)" stroke-width=".8"/><path d="M.8 5h8.4" stroke="var(--icon)" stroke-width=".8"/></svg>
    <span>www.murodeck.example</span>
  </div>
</section>
<svg class="flap" viewBox="0 0 78 289" aria-hidden="true">
  <path d="M0 .5 L68 24 Q77 28 77 38 L77 251 Q77 261 68 265 L0 288.5" fill="var(--paper)" stroke="var(--edge)" stroke-width="1"/>
</svg>

<!-- Business card, front -->
<section class="card card-front" aria-label="Business card front">
  <div class="stripe left">
    <span style="background:var(--navy)"></span><span style="background:var(--indigo)"></span><span style="background:var(--royal)"></span><span style="background:var(--ocean)"></span><span style="background:var(--azure)"></span><span style="background:var(--cyan)"></span><span style="background:var(--sky)"></span>
  </div>
  <div class="stripe right">
    <span style="background:var(--sky)"></span><span style="background:var(--cyan)"></span><span style="background:var(--azure)"></span><span style="background:var(--ocean)"></span><span style="background:var(--royal)"></span><span style="background:var(--indigo)"></span><span style="background:var(--navy)"></span>
  </div>
  <div class="wordmark">MuroDeck<br>Nordhaven</div>
  <div class="contact-line">
    <svg viewBox="0 0 10 10"><circle cx="5" cy="5" r="4.2" fill="none" stroke="var(--azure)" stroke-width="1"/><ellipse cx="5" cy="5" rx="1.8" ry="4.2" fill="none" stroke="var(--azure)" stroke-width=".8"/><path d="M.8 5h8.4" stroke="var(--azure)" stroke-width=".8"/></svg>
    <span>www.murodeck.example</span>
  </div>
</section>

<!-- Business card, back -->
<section class="card card-back" aria-label="Business card back">
  <div class="stripe left">
    <span style="background:var(--maroon)"></span><span style="background:var(--wine)"></span><span style="background:var(--wine)"></span><span style="background:var(--brick)"></span><span style="background:var(--ember)"></span>
  </div>
  <div class="stripe right">
    <span style="background:var(--ember)"></span><span style="background:var(--brick)"></span><span style="background:var(--wine)"></span><span style="background:var(--wine)"></span><span style="background:var(--maroon)"></span>
  </div>
  <div class="details">
    <div class="name">HENRIK SOLVANG</div>
    <div>+91 90000 41527</div>
    <svg class="pin" viewBox="0 0 10 10"><path d="M5 .5a3.3 3.3 0 0 0-3.3 3.3C1.7 6.3 5 9.5 5 9.5s3.3-3.2 3.3-5.7A3.3 3.3 0 0 0 5 .5z" fill="none" stroke="var(--amber)" stroke-width="1.2"/></svg>
    <div>Lorem Ipsum</div>
    <div>Dolor sit Amet, Consectetuer, Dolor sit Amet.</div>
    <div class="email"><svg viewBox="0 0 10 10"><rect x=".8" y="2" width="8.4" height="6" fill="none" stroke="var(--amber)" stroke-width="1"/><path d="M.8 2.3 5 5.6l4.2-3.3" fill="none" stroke="var(--amber)" stroke-width="1"/></svg><span>hello@murodeck.example</span></div>
  </div>
</section>

</body>
</html>
```